Vitamin and Nutrition Ecommerce Site Needs a High End Website Design

We need a new and improved Homepage design for a leading Vitamin eCommerce business.
We supply our customers worldwide with leading brands of vitamin supplements and nutritional products at discounted prices.
The site design and layout must improve sales conversion and maximize the user experience staying on the site!

We will need to see;
A New Nutri Harbour stylized font (no logo)
High-End Modern Design
Easy Sales Conversion Experience
Excellent Layout, Fast Navigation
Quality Font style, Stylish Colour Palette Selection
Appropriate Spacing
Call To Action to Improve Sales Conversion
Web page should Look Clean and Minimalist

The design should improve sales, communicate easy to find products, facilitate fast ordering, have a modern and professional appearance centered toward a predominately female consumer.

Thank you for your interest in this project!

Current design can be found on this link;
www.nutriharbour.com.au/nutri/

Target Market(s)

80% Female 30-65 years

Industry/Entity Type

Business

Number of Pages Required

1 page

Colors

Designer to choose colors to be used in the design.

Requirements
Must have
• design must result improve sales conversion
• new Nutri Harbour font design
• search field
• attractive clean modern design
• stylish font and colour palette selection
Nice to have
• white background
Should not have
• cluttered or busy layout
• confusing navigation

```html
<!DOCTYPE html>
<html lang="en">
<head>
<meta charset="utf-8">
<title>Nutri Harbour – Home</title>
<link href="https://fonts.googleapis.com/css2?family=Open+Sans:wght@400;600;700;800&family=Oswald:wght@500;600&display=swap" rel="stylesheet">
<style>
:root{
  --green:#7cb342;
  --green-dark:#5e9a2c;
  --orange:#f47b20;
  --teal:#3aa6b0;
  --teal-soft:#5cb9c2;
  --ink:#333;
  --muted:#888;
  --line:#e3e3e3;
  --footer:#f2f2f2;
  --white:#fff;
  --feature-ink:#2a6f97;
}
*{box-sizing:border-box;margin:0;padding:0}
html,body{width:771px;height:1200px;overflow:hidden;background:var(--white)}
body{font-family:"Open Sans",Arial,sans-serif;color:var(--ink);font-size:9px;position:relative}
.wrap{position:absolute;left:31px;width:709px}

/* top bar */
.topbar{position:absolute;top:0;left:0;width:771px;height:20px;border-bottom:1px solid var(--line);font-size:8px;color:var(--muted)}
.topbar .wrap{top:5px;display:flex;justify-content:space-between}
.topbar b{color:var(--green)}

/* header */
.header{position:absolute;top:20px;left:0;width:771px;height:64px}
.brand{position:absolute;left:31px;top:14px;display:flex;align-items:center;gap:7px;font-size:21px;font-weight:700;color:var(--green)}
.brand i{width:22px;height:22px;border-radius:50%;background:var(--green);display:block}
.search{position:absolute;left:300px;top:18px;width:175px;height:22px;border:1px solid #ccc;border-radius:3px;font-size:8px;color:var(--muted);padding:5px 8px}
.search svg{position:absolute;right:6px;top:5px}
.cart{position:absolute;right:31px;top:10px;width:64px;height:38px;background:var(--orange);color:#fff;font-size:7.5px;font-weight:700;padding:4px 4px 0 26px;line-height:10px;border-radius:2px}
.cart svg{position:absolute;left:7px;top:11px}

/* nav */
.nav{position:absolute;top:85px;left:0;width:771px;height:30px;background:var(--green)}
.nav ul{list-style:none;display:flex;position:absolute;left:31px;width:709px;height:30px}
.nav li{flex:1;color:#fff;font-size:8px;font-weight:700;text-align:center;padding-top:5px;line-height:10px;border-right:1px solid rgba(255,255,255,.25)}
.nav li.home{background:var(--green-dark);flex:.6;padding-top:10px}

/* hero */
.hero{position:absolute;top:115px;left:0;width:771px;height:322px;overflow:hidden}
.hero-photo{position:absolute;left:0;top:0;width:771px;height:322px;background:
  radial-gradient(ellipse 150px 170px at 240px 150px,#e9b98f 0%,#e2b083 40%,rgba(226,176,131,0) 75%),
  radial-gradient(ellipse 190px 150px at 260px 90px,#d9b878 0%,rgba(217,184,120,0) 80%),
  radial-gradient(ellipse 90px 70px at 190px 270px,#f5a53b 0%,rgba(245,165,59,0) 80%),
  linear-gradient(90deg,#c9bfb1 0%,#ded5c8 30%,#eee9e1 60%)}
.hero-panel{position:absolute;right:0;top:0;width:771px;height:322px}
.hero-copy{position:absolute;left:470px;top:26px;color:#fff;text-align:right;width:260px}
.hero-copy h2{font-family:"Oswald",sans-serif;font-size:36px;font-weight:600;line-height:40px}
.hero-copy h3{font-family:"Oswald",sans-serif;font-size:17px;font-weight:500;line-height:20px}
.hero-copy p{font-size:9px;margin-top:1px}
.hero-btn{position:absolute;left:632px;top:118px;background:#fff;color:var(--orange);font-weight:700;font-size:8px;padding:5px 12px;border-radius:2px}
.hero-products{position:absolute;left:470px;top:150px;width:270px;height:150px;background:
  linear-gradient(90deg,transparent 0 8%,#f5f5f0 8% 20%,transparent 20% 24%,#1f7a3a 24% 38%,transparent 38% 42%,#f2c21b 42% 56%,transparent 56% 60%,#eeeeea 60% 74%,transparent 74% 78%,#2e8b3e 78% 92%,transparent 92%) bottom/100% 62% no-repeat,
  linear-gradient(90deg,transparent 0 14%,#ffffff 14% 28%,transparent 28% 48%,#f4f4f0 48% 62%,transparent 62% 70%,#e7d48a 70% 84%,transparent 84%) top 18px left 0/100% 40% no-repeat}
.dots{position:absolute;left:345px;top:300px;display:flex;gap:5px}
.dots i{width:7px;height:7px;border-radius:50%;background:#fff;opacity:.6;display:block}
.dots i:first-child{opacity:1;background:var(--orange)}

/* promo tiles */
.promos{position:absolute;top:442px;left:31px;width:709px;height:128px;display:flex;gap:5px}
.tile{position:relative;flex:1;color:#fff;overflow:hidden}
.tile.offer{background:var(--orange)}
.tile.skin{background:var(--teal)}
.tile.hair{background:var(--teal-soft)}
.tile h4{position:absolute;left:12px;top:14px;font-size:11px;font-weight:800;line-height:13px}
.tile .big{position:absolute;left:12px;top:44px;font-size:22px;font-weight:800}
.tile .small{position:absolute;left:12px;top:76px;font-size:8px}
.tile .desc{position:absolute;left:12px;top:34px;width:92px;font-size:7px;line-height:10px;opacity:.9}
.tile .go{position:absolute;left:12px;bottom:10px;font-size:8px;font-weight:700}
.tile .visual{position:absolute;right:0;top:0;width:115px;height:128px}
.offer .visual{background:
  linear-gradient(90deg,transparent 0 8%,#7a4a1c 8% 34%,transparent 34% 38%,#8a5520 38% 64%,transparent 64% 68%,#7a4a1c 68% 94%,transparent 94%) center 70%/100% 55% no-repeat,
  linear-gradient(160deg,#2f2f2f,#55483a)}
.skin .visual{background:radial-gradient(ellipse 40px 55px at 60% 50%,#e9c4a8,rgba(233,196,168,0) 90%),linear-gradient(160deg,#e8d5c6,#c9a994)}
.hair .visual{background:radial-gradient(ellipse 45px 70px at 55% 55%,#b07a52,rgba(176,122,82,0) 90%),linear-gradient(160deg,#ecdccd,#d2b39c)}

/* tabs */
.tabs{position:absolute;top:590px;left:31px;width:709px;height:34px}
.tabs:before{content:"";position:absolute;left:0;right:0;top:17px;border-top:1px solid var(--line)}
.tabs ul{list-style:none;position:absolute;left:205px;display:flex;gap:4px}
.tabs li{width:96px;height:34px;line-height:34px;text-align:center;font-size:11px;background:#f1f1f1;color:#777;border:1px solid var(--line)}
.tabs li.on{background:var(--green);color:#fff;border-color:var(--green)}

/* products */
.products{position:absolute;top:636px;left:31px;width:709px;height:222px;display:flex;gap:14px;padding:0 22px}
.arrow{position:absolute;top:80px;font-size:14px;color:#aaa}
.arrow.l{left:4px}.arrow.r{right:4px}
.card{flex:1;position:relative;border:1px solid var(--line)}
.card .img{height:124px;margin:8px;background:#fff}
.img.pillow{background:radial-gradient(ellipse 38px 52px at 50% 50%,#e6eef4 0%,#cfdde8 70%,rgba(207,221,232,0) 100%),#fff}
.img.pillow2{background:radial-gradient(ellipse 36px 52px at 50% 50%,#eef0f3 0%,#d6dbe2 70%,rgba(214,219,226,0) 100%),#fff}
.img.tub{background:radial-gradient(ellipse 45px 45px at 50% 52%,#1f3d2c 0%,#14291d 70%,rgba(20,41,29,0) 100%),#fff}
.img.oil{background:radial-gradient(ellipse 22px 50px at 50% 55%,#a85d22 0%,#6e3a12 75%,rgba(110,58,18,0) 100%),#fff}
.card .name{font-size:8px;font-weight:600;padding:0 10px;line-height:11px;height:24px}
.card .was{position:absolute;left:10px;top:172px;font-size:7px;color:#aaa;text-decoration:line-through}
.card .price{position:absolute;left:10px;top:182px;font-size:12px;font-weight:700;color:var(--orange)}
.card .add{position:absolute;right:8px;top:182px;background:var(--orange);color:#fff;font-size:7px;font-weight:700;padding:4px 7px}

/* features */
.features{position:absolute;top:873px;left:31px;width:709px;height:42px;display:flex;gap:5px}
.feat{flex:1;background:#eaf4fb;display:flex;align-items:center;gap:7px;padding:0 10px}
.feat svg{flex:none}
.feat b{font-size:8px;font-weight:800;color:var(--feature-ink);display:block}
.feat span{font-size:6.5px;color:var(--muted)}

/* rewards */
.rewards{position:absolute;top:937px;left:31px;width:709px;height:52px;border-top:1px solid var(--line);border-bottom:1px solid var(--line)}
.rewards h5{position:absolute;left:0;top:12px;font-size:10px;font-weight:800;line-height:12px}
.rewards p{position:absolute;left:168px;top:14px;width:220px;font-size:7px;line-height:10px;color:var(--muted)}
.rewards .field{position:absolute;left:430px;top:14px;width:215px;height:22px;border:1px solid #ccc;font-size:7px;color:#aaa;padding:6px 8px}
.rewards .join{position:absolute;right:0;top:14px;width:58px;height:22px;background:#222;color:#fff;font-size:8px;font-weight:700;text-align:center;line-height:22px}

/* footer */
.footer{position:absolute;top:1000px;left:0;width:771px;height:172px;background:var(--footer)}
.cols{position:absolute;left:31px;top:14px;width:709px;display:flex}
.col{flex:1}
.col h6{font-size:8px;font-weight:800;margin-bottom:6px}
.col li{list-style:none;font-size:7px;color:#777;line-height:11px}
.social{display:flex;gap:4px;margin-bottom:10px}
.social i{width:16px;height:16px;border-radius:50%;background:#9a9a9a;display:block}
.cards{display:flex;gap:4px;flex-wrap:wrap;width:110px}
.cards i{width:24px;height:15px;border-radius:2px;background:#cfcfcf;display:block}
.copyright{position:absolute;top:1172px;left:0;width:771px;height:28px;text-align:center;font-size:7px;color:var(--muted);line-height:28px}
</style>
</head>
<body>

<div class="topbar"><div class="wrap"><span>Get your <b>FREE</b> Phone Code Here</span><span>My Account &nbsp;|&nbsp; Login &nbsp;|&nbsp; Register &nbsp;|&nbsp; Wish List</span></div></div>

<header class="header">
  <div class="brand"><i></i>Nutri Harbour</div>
  <div class="search">Search entire store here...
    <svg width="11" height="11" viewBox="0 0 11 11"><circle cx="4.5" cy="4.5" r="3.5" fill="none" stroke="#888" stroke-width="1.4"/><line x1="7" y1="7" x2="10" y2="10" stroke="#888" stroke-width="1.4"/></svg>
  </div>
  <div class="cart">
    <svg width="14" height="13" viewBox="0 0 14 13"><path d="M0 1h3l2 7h7l2-5H4" fill="none" stroke="#fff" stroke-width="1.3"/><circle cx="6" cy="11" r="1.2" fill="#fff"/><circle cx="11" cy="11" r="1.2" fill="#fff"/></svg>
    MY CART<br>0 item(s)<br>$0.00
  </div>
</header>

<nav class="nav"><ul>
  <li class="home">HOME</li>
  <li>SUPPLEMENTS &amp;<br>VITAMINS</li>
  <li>SPORTS<br>NUTRITION</li>
  <li>HAIRCARE &amp;<br>BEAUTY</li>
  <li>CHIROPRACTIC<br>PILLOWS</li>
  <li>HEALTH<br>CONDITION</li>
  <li>BEAUTY &amp;<br>SKINCARE</li>
  <li>WEIGHT<br>LOSS</li>
  <li>SPECIALS<br>&amp; DEALS</li>
</ul></nav>

<section class="hero">
  <div class="hero-photo" role="img" aria-label="Smiling woman holding a glass of orange juice in a bright kitchen"></div>
  <svg class="hero-panel" viewBox="0 0 771 322" aria-hidden="true"><polygon points="440,0 771,0 771,322 360,322" fill="#f47b20"/></svg>
  <div class="hero-copy">
    <h2>EXTRA 20% OFF</h2>
    <h3>VITAMINS SUPPLEMENTS</h3>
    <p>Use promo code: HARBOUR20</p>
  </div>
  <div class="hero-btn">SHOP NOW ›</div>
  <div class="hero-products" role="img" aria-label="Group of vitamin supplement bottles with yellow, green and white labels"></div>
  <div class="dots"><i></i><i></i><i></i><i></i></div>
</section>

<section class="promos">
  <div class="tile offer">
    <h4>EXCLUSIVE<br>OFFERS</h4>
    <div class="big">15% OFF</div>
    <div class="small">Daily B Complex</div>
    <div class="go">SHOP NOW ›</div>
    <div class="visual" role="img" aria-label="Three amber vitamin B complex bottles"></div>
  </div>
  <div class="tile skin">
    <h4>SKINCARE</h4>
    <div class="desc">Gentle daily care for radiant, healthy and nourished looking skin.</div>
    <div class="go">SHOP NOW ›</div>
    <div class="visual" role="img" aria-label="Woman with clear glowing skin"></div>
  </div>
  <div class="tile hair">
    <h4>HAIRCARE</h4>
    <div class="desc">Strengthen and restore shine with our natural hair treatments.</div>
    <div class="go">SHOP NOW ›</div>
    <div class="visual" role="img" aria-label="Woman with long glossy hair"></div>
  </div>
</section>

<div class="tabs"><ul><li class="on">Featured Product</li><li>New Arrivals</li><li>Our Best Sellers</li></ul></div>

<section class="products">
  <span class="arrow l">‹</span><span class="arrow r">›</span>
  <div class="card"><div class="img pillow" role="img" aria-label="Boxed white contoured pillow"></div><div class="name">Calmrest Pillow Small Size Soft Density</div><span class="was">$109.00</span><span class="price">$95.00</span><span class="add">ADD TO CART</span></div>
  <div class="card"><div class="img pillow2" role="img" aria-label="Boxed white contoured pillow, super soft"></div><div class="name">Calmrest Pillow Standard Size Super Soft Density</div><span class="was">$109.00</span><span class="price">$95.00</span><span class="add">ADD TO CART</span></div>
  <div class="card"><div class="img tub" role="img" aria-label="Dark green supplement tub"></div><div class="name">Deep Rest Deluxe Conventional Foam</div><span class="was">$29.00</span><span class="price">$19.99</span><span class="add">ADD TO CART</span></div>
  <div class="card"><div class="img oil" role="img" aria-label="Amber essential oil bottle"></div><div class="name">Cedarwood Oil</div><span class="was">$14.00</span><span class="price">$11.99</span><span class="add">ADD TO CART</span></div>
</section>

<section class="features">
  <div class="feat"><svg width="20" height="14" viewBox="0 0 20 14"><rect x="0" y="2" width="12" height="8" fill="#2a6f97"/><path d="M12 5h4l3 3v2h-7z" fill="#2a6f97"/><circle cx="4" cy="12" r="2" fill="#2a6f97"/><circle cx="15" cy="12" r="2" fill="#2a6f97"/></svg><div><b>FREE SHIPPING</b><span>for all orders over $99</span></div></div>
  <div class="feat"><svg width="16" height="16" viewBox="0 0 16 16"><circle cx="8" cy="8" r="7" fill="#2a6f97"/><path d="M4.5 8l2.5 2.5 4.5-5" stroke="#fff" stroke-width="1.6" fill="none"/></svg><div><b>OFFICIAL STOCKIST</b><span>of more than 100 brands</span></div></div>
  <div class="feat"><svg width="16" height="16" viewBox="0 0 16 16"><rect x="1" y="6" width="14" height="9" fill="#2a6f97"/><rect x="0" y="3" width="16" height="4" fill="#2a6f97"/><rect x="7" y="3" width="2" height="12" fill="#fff"/></svg><div><b>2 FREE SAMPLES</b><span>on all orders with us</span></div></div>
  <div class="feat"><svg width="16" height="16" viewBox="0 0 16 16"><path d="M8 1l6 2v5c0 4-3 6-6 7-3-1-6-3-6-7V3z" fill="#2a6f97"/></svg><div><b>SAFESHOP TRUSTED STORE</b><span>rating of 4.9 out of 5</span></div></div>
</section>

<section class="rewards">
  <h5>JOIN<br>NUTRI HARBOUR REWARDS</h5>
  <p>Be rewarded with exclusive member offers, including discounts, sales, freebies, gifts with purchase and competitions.</p>
  <div class="field">Enter your email address</div>
  <div class="join">JOIN</div>
</section>

<footer class="footer">
  <div class="cols">
    <div class="col"><h6>CUSTOMER SERVICE</h6><ul><li>Contact Us</li><li>Help &amp; FAQ</li><li>Order Tracking</li><li>Return Policy</li><li>Shipping Information</li><li>Shopping Cart</li><li>International Orders</li></ul></div>
    <div class="col"><h6>ABOUT US</h6><ul><li>Company Information</li><li>Employment</li><li>Affiliate Program</li><li>100% Lowest Price Guarantee</li><li>100% Happiness Guarantee</li><li>Our Family Of Brands</li><li>Company News</li></ul></div>
    <div class="col"><h6>SAFE &amp; SECURE SHOPPING</h6><ul><li>Security Privacy</li><li>Terms &amp; Conditions</li><li>Secure Certificate Privacy Rights</li><li>Site Map</li><li>Safety News</li></ul></div>
    <div class="col" style="flex:.8"><h6>FOLLOW US</h6><div class="social"><i></i><i></i><i></i><i></i><i></i></div><h6>WE ACCEPT</h6><div class="cards"><i></i><i></i><i></i><i></i></div></div>
  </div>
</footer>
<div class="copyright">© 2017 NUTRI HARBOUR. ALL RIGHTS RESERVED</div>

</body>
</html>
```